Packaging Design for Boneless Picnic Ham

We are Bright Larder Limited, a company based in Trinidad which is located within the Caribbean. We produce and sell a plethora of meat products including a variety of hams, sausages and even bacon.

We require a packaging design for a ham product. This product is packaged within a cryovac (11" X 18") shrink bag which would be used to package our Boneless Picnic Ham which weighs 2.5 Kilograms.

The design space should be 7 inches wide and 6 inches in height. The design is 3 inches from the bottom and 2 inches off each side.

Our target audience comprises of caterers as well as the average household folk. What sets our product apart is that it is has a great taste, 20% less salt and is affordable and easy. We commonly refer to it as the "Oven Ready Roast".

Attached below, is our logo which you must incorporate onto the design. We also request that the header be "Applewood Cured Rolled Country Pork".

Target Market(s)

Caterers and Average Household Folk

Industry/Entity Type

It Company

Font styles to use
Sans Serif

Requirements
Must have
• The Bright Larder Company Logo and the header must have "Applewood Cured Rolled Country Pork"
Nice to have
• Maximum Creativity
Should not have
• No animal artwork should be included onto the design

```html
<!DOCTYPE html>
<html lang="en">
<head>
<meta charset="utf-8">
<title>Bright Larder – Boneless Picnic Ham Label</title>
<link href="https://fonts.googleapis.com/css2?family=Roboto+Condensed:wght@300;700&family=Oswald:wght@600&family=Tinos:wght@400;700&display=swap" rel="stylesheet">
<style>
  :root {
    --page: #f6f6f6;
    --orange: #e99f2c;
    --orange-light: #f2bb45;
    --gold: #f3cf62;
    --gold-deep: #c0851f;
    --gold-pale: #fff1b0;
    --red: #a8182a;
    --red-deep: #6e0a16;
    --navy: #27338a;
    --navy-deep: #0f164d;
    --cream-yellow: #f3d66e;
    --black: #141414;
  }
  * { box-sizing: border-box; margin: 0; padding: 0; }
  html, body { width: 1200px; height: 1200px; overflow: hidden; background: var(--page); }
  .canvas { position: relative; width: 1200px; height: 1200px; }

  .label {
    position: absolute; left: 108px; top: 180px; width: 984px; height: 842px;
    background: radial-gradient(ellipse at 50% 55%, var(--orange-light) 0%, var(--orange) 70%);
    border: 4px solid var(--gold);
    box-shadow: 0 120px 40px -100px rgba(0,0,0,0.35);
    overflow: hidden;
  }
  .label__frame {
    position: absolute; inset: 12px;
    border: 2px solid var(--gold-deep);
    pointer-events: none;
  }
  .centre-band {
    position: absolute; left: 254px; top: -4px; width: 478px; height: 850px;
    background: linear-gradient(180deg, var(--red-deep) 0%, var(--red) 45%, var(--red) 100%);
    border-left: 8px solid var(--gold);
    border-right: 8px solid var(--gold);
  }
  .brand-backdrop { position: absolute; left: 264px; top: 16px; width: 436px; height: 212px; }
  .brand-name {
    position: absolute; left: 264px; top: 92px; width: 436px; text-align: center;
    font-family: "Roboto Condensed", sans-serif; font-weight: 700; font-size: 48px;
    color: var(--navy);
  }
  .product-title {
    position: absolute; left: 282px; top: 230px; width: 422px; text-align: center;
    background: linear-gradient(180deg, var(--gold-pale) 0%, var(--gold) 50%, var(--gold-deep) 100%);
    -webkit-background-clip: text; background-clip: text; color: transparent;
  }
  .product-title__light {
    display: block; font-family: "Roboto Condensed", sans-serif; font-weight: 300;
    font-size: 92px; line-height: 84px;
  }
  .product-title__bold {
    display: block; font-family: "Oswald", sans-serif; font-weight: 600;
    font-size: 86px; line-height: 96px; letter-spacing: 1px;
  }
  .product-header {
    position: absolute; left: 270px; top: 414px; width: 446px; text-align: center;
    font-family: "Roboto Condensed", sans-serif; font-weight: 700; font-size: 21px;
    letter-spacing: 1px; color: var(--gold);
  }
  .product-photo {
    position: absolute; left: 246px; top: 452px; width: 530px; height: 370px;
    border-radius: 50% 45% 35% 40% / 55% 50% 30% 35%;
    background: radial-gradient(ellipse at 40% 45%, rgba(176,66,40,0.95) 0%, rgba(150,44,30,0.85) 45%, rgba(214,150,140,0.55) 75%, rgba(214,150,140,0) 100%);
  }
  .weight-badge {
    position: absolute; left: 112px; top: 626px; width: 156px; height: 220px;
    background: linear-gradient(180deg, var(--navy) 0%, var(--navy-deep) 100%);
    border: 3px solid var(--gold); border-bottom: none; border-radius: 10px 10px 0 0;
    text-align: center; color: #fff; font-family: "Oswald", sans-serif; font-weight: 600;
  }
  .weight-badge__label { display: block; margin-top: 22px; font-size: 38px; line-height: 40px; }
  .weight-badge__value {
    display: block; font-size: 104px; line-height: 92px;
    background: linear-gradient(180deg, var(--gold-pale), var(--gold-deep));
    -webkit-background-clip: text; background-clip: text; color: transparent;
  }
  .weight-badge__unit { display: block; font-size: 25px; line-height: 28px; }
  .classic-ribbon { position: absolute; left: 862px; top: -4px; width: 60px; height: 398px; }
  .classic-ribbon__text {
    position: absolute; left: 862px; top: 100px; width: 60px; height: 200px;
    display: flex; align-items: center; justify-content: center;
    font-family: "Tinos", serif; font-size: 40px; color: var(--gold); letter-spacing: 1px;
  }
  .classic-ribbon__text span { transform: rotate(-90deg); white-space: nowrap; }
  .quality-seal {
    position: absolute; left: 766px; top: 536px; width: 152px; height: 152px; border-radius: 50%;
    background: radial-gradient(circle at 40% 35%, #3a3a3a, var(--black) 70%);
    border: 5px solid var(--gold);
    box-shadow: 0 0 0 2px var(--gold-deep), 4px 6px 10px rgba(0,0,0,0.3);
    display: flex; align-items: center; justify-content: center;
  }
  .quality-seal__text {
    transform: rotate(-14deg); text-align: center; font-family: "Tinos", serif; font-weight: 700;
    color: var(--gold); font-size: 34px; line-height: 34px;
  }
</style>
</head>
<body>
<div class="canvas">
  <div class="label">
    <div class="label__frame"></div>
    <div class="centre-band"></div>

    <svg class="brand-backdrop" viewBox="0 0 436 212" role="img" aria-label="Checked cloth backdrop behind brand name">
      <polygon points="0,96 160,0 436,110 300,212" fill="var(--cream-yellow)"/>
    </svg>
    <div class="brand-name">Bright Larder</div>

    <h1 class="product-title">
      <span class="product-title__light">BONELESS</span>
      <span class="product-title__bold">PICNICHAM</span>
    </h1>
    <p class="product-header">APPLEWOOD CURED ROLLED COUNTRY PORK</p>

    <div class="product-photo" role="img" aria-label="Whole glazed boneless picnic ham with sliced rounds and red berries"></div>

    <div class="weight-badge">
      <span class="weight-badge__label">WEIGHS</span>
      <span class="weight-badge__value">2.5</span>
      <span class="weight-badge__unit">KILOGRAMS</span>
    </div>

    <svg class="classic-ribbon" viewBox="0 0 60 398" aria-hidden="true">
      <polygon points="0,0 60,0 60,398 30,374 0,398" fill="var(--gold)"/>
      <polygon points="5,0 55,0 55,386 30,366 5,386" fill="var(--red-deep)"/>
    </svg>
    <div class="classic-ribbon__text"><span>CLASSIC</span></div>

    <div class="quality-seal">
      <div class="quality-seal__text">Quality<br>No.1</div>
    </div>
  </div>
</div>
</body>
</html>
```